Automotive Repair Centre - Flyer Design

Bremwick Motors Cumbernauld are looking for a completely new flyer design for our blossoming auto repair centre. We are looking for bold eye catching designs as these flyers will be letterbox dropped around the local community. Approx. 10k per month. These will be printed double sided, on A5, with different print front and rear. Currently the whole rear is dedicated to servicing only, but this can be changed.

Our business prides itself on providing a high quality service so they flyer needs to convey this message. Also we believe in fair prices so they flyer also needs to convey this message in the design. Colour scheme is currently blue, yellow, and black. If possible it would be good to include the Drivemarq logo and the KELP logo.

We like the "specials" list from the Halvorn Drake flyer that is attached. We also like the clean look and layout of the other flyer that is uploaded. It would be good to include a special area for winter tyres much like is shown in the 50% off wheel alignment piece of the flyer attached.

Our current flyer uses the font GoodTimes as we would like this to remain if possible. It can be changed if the designer prefers. You can visit our website www.bremwick.co.uk for more information about our business.
Updates

Reason: Not had enough good designs to choose from yet.

Reason: Still not enough good designs to choose from

Reason: designs not up to the standard required.

Reason: Not enough designs that capture the brief have been submitted

Reason: looking for more designs

Reason: looking for some more bright designs. please read the brief!!!

Reason: same as before

Target Market(s)

General public.

Industry/Entity Type

Wheel

Requirements
Should not have
• We feel the flyer should not have photos of high end vehicles like Zantellis etc as the does not fit our approach of good value.

```html
<!DOCTYPE html>
<html lang="en">
<head>
<meta charset="utf-8">
<title>Bremwick Motors Cumbernauld – Flyer</title>
<link rel="stylesheet" href="https://fonts.googleapis.com/css2?family=Orbitron:wght@500;700&family=Exo+2:ital,wght@1,800&family=Montserrat:wght@600&display=swap">
<style>
  :root {
    --black: #0c0c0d;
    --hero-dark: #1d1b1c;
    --hero-mid: #3a3636;
    --blue: #0a6fc9;
    --blue-light: #1aa3ee;
    --blue-deep: #0649a0;
    --yellow: #f6ea1a;
    --dot: #f2c84b;
    --white: #ffffff;
  }
  * { margin: 0; padding: 0; box-sizing: border-box; }
  html, body { width: 856px; height: 1200px; overflow: hidden; background: var(--black); }
  .flyer { position: relative; width: 856px; height: 1200px; background: var(--black); overflow: hidden; color: var(--white); }

  .hero {
    position: absolute; left: 0; top: 0; width: 856px; height: 470px;
    background: radial-gradient(ellipse at 55% 35%, var(--hero-mid) 0%, var(--hero-dark) 55%, var(--black) 100%);
  }
  .body-fade {
    position: absolute; left: 0; top: 420px; width: 856px; height: 386px;
    background: linear-gradient(180deg, rgba(29,27,28,0) 0%, #1a1819 30%, #141213 100%);
  }

  .tagline-band {
    position: absolute; left: 290px; top: 0; width: 566px; height: 89px;
    background: linear-gradient(90deg, var(--blue-deep) 0%, var(--blue-light) 45%, var(--blue) 100%);
    clip-path: polygon(0 0, 100% 0, 100% 100%, 42px 100%);
  }
  .tagline {
    position: absolute; right: 44px; top: 22px;
    font-family: "Exo 2", sans-serif; font-style: italic; font-weight: 800;
    font-size: 37px; letter-spacing: -0.5px; white-space: nowrap;
  }
  .tagline .accent { color: var(--yellow); }

  .brand {
    position: absolute; left: 150px; top: 215px;
    display: flex; align-items: center; gap: 22px;
  }
  .brand-dot { width: 40px; height: 40px; border-radius: 50%; background: var(--yellow); }
  .brand-name {
    font-family: "Orbitron", sans-serif; font-weight: 700; font-size: 78px;
    color: var(--white); letter-spacing: 1px; line-height: 1;
  }

  .services { position: absolute; left: 54px; top: 440px; list-style: none; }
  .services li {
    display: flex; align-items: center; height: 56px;
    font-family: "Orbitron", sans-serif; font-weight: 500; font-size: 37px;
    letter-spacing: 1px; white-space: nowrap;
  }
  .services li::before {
    content: ""; width: 24px; height: 24px; border-radius: 50%;
    background: var(--yellow); margin-right: 22px; flex: none;
  }

  .extras { position: absolute; right: 66px; top: 588px; text-align: right; }
  .extras-title {
    font-family: "Orbitron", sans-serif; font-weight: 500; font-size: 22px;
    color: var(--yellow); letter-spacing: 1px; margin-bottom: 14px; margin-right: 8px;
  }
  .extras ul { list-style: none; }
  .extras li {
    font-family: "Orbitron", sans-serif; font-weight: 500; font-size: 21px;
    letter-spacing: 1px; height: 29px; line-height: 29px; white-space: nowrap;
  }
  .extras li::after {
    content: ""; display: inline-block; width: 11px; height: 11px; border-radius: 50%;
    background: var(--dot); margin-left: 12px; vertical-align: middle;
  }

  .photo-band {
    position: absolute; left: 0; top: 806px; width: 856px; height: 222px;
    background: linear-gradient(180deg, var(--blue-light) 0%, var(--blue) 45%, var(--blue-deep) 100%);
  }
  .photo { position: absolute; top: 24px; height: 174px; }
  .photo-diagnostics { left: 0; width: 235px; background: linear-gradient(135deg, #2a3440 0%, #7a2a2a 50%, #5f86b0 100%); }
  .photo-mechanic { left: 247px; width: 297px; background: linear-gradient(135deg, #2b2f38 0%, #4d6d9a 55%, #20242b 100%); }
  .photo-spanner { left: 556px; width: 300px; background: linear-gradient(135deg, #3b3b3d 0%, #9b7a62 45%, #5c5f66 100%); }

  .footer { position: absolute; left: 0; top: 1028px; width: 856px; height: 151px; background: var(--black); }
  .address {
    position: absolute; left: 73px; top: 42px;
    font-family: "Montserrat", sans-serif; font-weight: 600; font-size: 16.5px; line-height: 22px;
  }
  .address .pin { position: absolute; left: -17px; top: 4px; }
  .phone {
    position: absolute; left: 380px; top: 48px; display: flex; align-items: center; gap: 10px;
    font-family: "Orbitron", sans-serif; font-weight: 700; font-size: 38px; color: var(--yellow);
    letter-spacing: 2px;
  }
  .contact {
    position: absolute; top: 113px; display: flex; align-items: center; gap: 7px;
    font-family: "Montserrat", sans-serif; font-weight: 600; font-size: 16.5px;
  }
  .contact-email { left: 368px; }
  .contact-web { left: 622px; }
  .stripe { position: absolute; left: 0; top: 1179px; width: 856px; height: 21px; background: var(--yellow); }
</style>
</head>
<body>
<main class="flyer">
  <div class="hero" role="img" aria-label="Dimly lit photo of the repair centre building at dusk"></div>
  <div class="body-fade"></div>

  <div class="tagline-band"></div>
  <p class="tagline">YOU DRIVE <span class="accent">IT</span> WE FIX <span class="accent">IT</span></p>

  <div class="brand">
    <span class="brand-dot"></span>
    <span class="brand-name">BREMWICK</span>
  </div>

  <ul class="services">
    <li>MOT $35</li>
    <li>SERVICING $89</li>
    <li>TYRES</li>
    <li>BRAKES</li>
    <li>EXHAUSTS</li>
    <li>CLUTCHES</li>
  </ul>

  <section class="extras">
    <h2 class="extras-title">WE ALSO PROVIDE:</h2>
    <ul>
      <li>FAULT DIAGNOSTICS</li>
      <li>BATTERIES</li>
      <li>WHEEL ALIGNMENT</li>
      <li>WELDING</li>
      <li>&amp; MORE</li>
    </ul>
  </section>

  <section class="photo-band">
    <div class="photo photo-diagnostics" role="img" aria-label="Gloved hands holding a diagnostic tablet under a car bonnet"></div>
    <div class="photo photo-mechanic" role="img" aria-label="Mechanic in blue shirt working beneath a raised car"></div>
    <div class="photo photo-spanner" role="img" aria-label="Hands using a spanner on an engine"></div>
  </section>

  <footer class="footer">
    <address class="address" style="font-style:normal">
      <svg class="pin" width="11" height="15" viewBox="0 0 11 15"><path d="M5.5 0C2.5 0 0 2.4 0 5.4 0 9.3 5.5 15 5.5 15S11 9.3 11 5.4C11 2.4 8.5 0 5.5 0zm0 7.6a2.2 2.2 0 1 1 0-4.4 2.2 2.2 0 0 1 0 4.4z" fill="#f6ea1a"/></svg>
      14 Harlow Court<br>Brackenfield Business Park<br>Cumbernauld<br>G67 4QZ
    </address>
    <div class="phone">
      <svg width="38" height="38" viewBox="0 0 38 38"><circle cx="19" cy="19" r="17" fill="none" stroke="#fff" stroke-width="2"/><path d="M14 10c1.5-1 2.5-.5 3 .8l1.4 3.5c.4 1-.1 1.8-1 2.3l-1.2.7c.8 2.8 2.4 5 4.6 6.6l1-1c.8-.7 1.7-.8 2.5 0l2.6 2.4c.9.9.8 2-.3 2.9-2.2 1.8-5 1.4-7.6-.8-3.6-3-6-7.2-6.3-11.4-.1-2.4.6-4.3 1.3-6z" fill="#fff"/></svg>
      <span>01236 555018</span>
    </div>
    <div class="contact contact-email">
      <svg width="18" height="13" viewBox="0 0 18 13"><rect x="1" y="1" width="16" height="11" fill="none" stroke="#f6ea1a" stroke-width="1.6"/><path d="M1 1l8 6 8-6" fill="none" stroke="#f6ea1a" stroke-width="1.6"/></svg>
      <span>sales@bremwick.co.uk</span>
    </div>
    <div class="contact contact-web">
      <svg width="17" height="17" viewBox="0 0 17 17" fill="none" stroke="#f6ea1a" stroke-width="1.3"><circle cx="8.5" cy="8.5" r="7.5"/><ellipse cx="8.5" cy="8.5" rx="3.4" ry="7.5"/><path d="M1 8.5h15M2.5 4.5h12M2.5 12.5h12"/></svg>
      <span>www.bremwick.co.uk</span>
    </div>
  </footer>
  <div class="stripe"></div>
</main>
</body>
</html>
```